Wavelume artwork for new single release

I need Wavelume artwork creating to release a new single on there.

The specs are:

Ideal size: 3000 x 3000 pixels
Minimum size: 1400 x 1400 pixels
Aspect ratio: 1:1 (must be a perfect square)
File format: JPG or PNG
Color space: sRGB
File size: Max 4MB

The song is called "Still, Can We Wander?"
The artist is "Milo Fenwright"

We have no images of Milo, so it really is open to imagination.

Target Market(s)

Wavelume listeners

Industry/Entity Type

Music

```html
<!DOCTYPE html>
<html lang="en">
<head>
<meta charset="utf-8">
<title>Milo Fenwright – Still, Can We Wander?</title>
<link rel="stylesheet" href="https://fonts.googleapis.com/css2?family=Alfa+Slab+One&family=Courier+Prime:wght@700&family=Montserrat:wght@400&display=swap">
<style>
  :root {
    --paper: #ffffff;
    --ink: #000000;
    --heart-red: #ed2c25;
  }
  html, body {
    margin: 0;
    padding: 0;
    width: 1200px;
    height: 1200px;
    overflow: hidden;
    background: var(--paper);
  }
  .cover {
    display: block;
    width: 1200px;
    height: 1200px;
  }
  .artist-name {
    font-family: "Montserrat", sans-serif;
    font-weight: 400;
    font-size: 100px;
  }
  .artist-name--shadow { fill: var(--ink); }
  .artist-name--face { fill: var(--heart-red); }
  .title-display {
    font-family: "Alfa Slab One", serif;
    font-size: 400px;
    fill: var(--ink);
  }
  .title-tail {
    font-family: "Courier Prime", monospace;
    font-weight: 700;
    font-size: 250px;
    fill: var(--ink);
  }
  .title-heart { fill: var(--heart-red); }
</style>
</head>
<body>
<svg class="cover" viewBox="0 0 1200 1200" xmlns="http://www.w3.org/2000/svg" role="img" aria-label="Milo Fenwright – Still, Can We Wander?">
  <rect width="1200" height="1200" fill="var(--paper)"/>

  <g class="artist">
    <text class="artist-name artist-name--shadow" x="127" y="164" textLength="930" lengthAdjust="spacingAndGlyphs">MILO FENWRIGHT</text>
    <text class="artist-name artist-name--face" x="125" y="154" textLength="930" lengthAdjust="spacingAndGlyphs">MILO FENWRIGHT</text>
  </g>

  <g class="title">
    <text class="title-display" x="120" y="555" textLength="920" lengthAdjust="spacingAndGlyphs">STILL,</text>

    <text class="title-display" x="120" y="925" textLength="180" lengthAdjust="spacingAndGlyphs">C</text>
    <path class="title-heart" transform="translate(318 640) scale(3 3)"
          d="M50,95 C20,78 0,55 0,30 C0,10 15,0 28,0 C40,0 48,8 50,12 C52,8 60,0 72,0 C88,0 100,12 100,30 C100,55 78,78 50,95 Z"/>
    <text class="title-display" x="640" y="925" textLength="420" lengthAdjust="spacingAndGlyphs">N WE</text>

    <text class="title-tail" x="122" y="1119" textLength="935" lengthAdjust="spacingAndGlyphs">WANDER?</text>
  </g>
</svg>
</body>
</html>
```